Yoga/movement guide/teacher for adult yoga practice and kid yoga

What is the positioning or mission statement of your company? to guide individuals in a yoga-based safe and sustainable movement practice applicable to all ages and body types. Currently my focus is working with children in daycare and school settings, but my goal is to expand into private yoga practice for adults, and potentially as part of rented space in studios. I hope to find a way to work with children AND adults (so would love for logo to be appealing to both), but current focus is with children based on need and demand in the community. yoga for children also compliments my backround as a pediatrician/neonatologist, and I greatly miss interacting with children. I also want to emphasize a yoga/movement practice that is focused more on what one feels internally through movement. NOT what one looks like asthetically. I believe in removing all mirrors from yoga/movement practice. It should be an experience of movement/poses/yoga through appropriate cueing and education. It is not about the details of how far the knee should bend, or how high the leg should be. Focusing on foudation first, core, then core engagement and ultimately expression of poses/movements. A focus on strength, stability and mobility, not just flexibility, which is the common perception/association with yoga. I also want individuals to learn to be an advocate of their own health. Through guidance, I hope for individuals to connect with their body so they know themselves so well to be able to advocate for themselves in the modern healthcare world. This internal experience and connection is so essential in a world where modern medicine has become a business and it is all about making a dollar. the connection with patients is lost, and individuals need to learn to empower themselves and through their new found voice to be able to articulate what is wrong.<br/>Does your company have a tagline or slogan that should be included with the logo? "Practice Radiant Movement"<br/>What do you hope your company can be known for? Accessible yoga for a sustained practice. A guided movement practice where one gains information and knowledge of oneself through a mind/body connection. For one feel good physically with a new awaraness of their internal radiance that exists in all beings. Physical rejuvenation egnites a light and increases energy to flow through the physical body, which ultimately tranlates into works of kindness for others and out in the world. <br/>What color palettes might you prefer? why? love the colors currently chosen<br/>Where will the logo be primarily used? initially business cards, but hopefully future websites, t-shirts, and potentially local magazine adds. Also starting with a small couple of banners for community events in the area. I currently practice as a nomad out of my car :)<br/>Are there any elements you would prefer to see in the logo? Movement. A modern depiction of a human body/figure practicing movement. Hoping to avoid a stereotypical yoga pose per say, just because I want to people to think of it more of a movement practice with yoga roots. Modern yoga. There are elements of breathing and connecting with oneself through the flow of breath and movement, but I do not focus on the meditative/cerebral aspect of the yoga practice. What I teach is almost reaching a meditative state through movement. I personally don't practice, nor resonate with just seated meditation. just not my thing :)<br/>In your opinion, what defines a well-designed logo? curiosity. enough info for individuals to think they know what it means, but want to know more. invokes curiosity, but not too abstract. Reproducible. not too complicated. I want also to invoke a community feel, so a design that appeals to all people within a community. <br/>What is your preference in reference to icons, typography, spokespeople (characters), etc.? modern design. I love the idea of a logo for my purposes, to invoke a sense of movement from within. So not too static. <br/>What words or icons must be included in the logo? movement with yoga roots. <br/>What logos do you like and why? A representation, but not exact. I think some ambiguity is intriguing for others, and also memorable. I want it to be an artistic representation of movement/yoga<br/>What logos do you dislike and why? too busy, too loud. <br/>In your opinion, what is the primary purpose for a logo? association<br/>Who is the primary target audience? (who is most likely to use your services/product?) Children and their parents, but ultimately to expand into teaching adults. I even have aspirations of prenatal and post-natal yoga. Potentially incorporating infants. <br/>Who currently uses your product the most? n/a (working in schools/daycare currently. It is currently all volunteer)<br/>Are you pleased with the range of people your company serves? n/a<br/>Are you looking to expand, modify, or completely change your target audience? or will it remain the same? yes! expand into an adult audience. <br/>How do you plan to focus on your target audience? currently by working through schools and daycares. hopefully ultimately through after school care programs and then offering kid yoga in an existing yoga studio (working on this with Quillbrook in Ridgeland, currently)<br/>What are your main forms of advertising? word of mouth, schools, daycares. Happy kids talking to their parents about the yoga class they took and happy teachers :)<br/>How do most customers find out about your company?<br/>Which gender are you targeting? All genders! However, with kid yoga, often the maternal individual in the child's life is more involved with decision making as far as extracurricular activities

Target Market(s)

individuals and families interested in wellness and feeling great

Contact Information for Business Card

Dana Whitford
Yoga Instructor
RYT-200, RCYT

certified yoga teacher for adults and children

Colors

Requirements
Must have
• "Practice Radiant Movement"
Nice to have
• logo with same colors

```html
<!DOCTYPE html>
<html lang="en">
<head>
<meta charset="UTF-8">
<title>Radiant Rise – Business Card</title>
<link rel="stylesheet" href="https://fonts.googleapis.com/css2?family=Domine:wght@400;700&family=Lora:wght@400&display=swap">
<style>
  :root {
    --backdrop: #2b2e33;
    --card-white: #ffffff;
    --sun-yellow: #ffc42a;
    --sun-yellow-deep: #f5b514;
    --ornament-yellow: #fdd23e;
    --ink: #3a3a3a;
    --ink-soft: #555555;
    --paper-white: #ffffff;
  }
  * { box-sizing: border-box; margin: 0; padding: 0; }
  html, body { width: 1200px; height: 900px; overflow: hidden; }
  body { background: var(--backdrop); position: relative; font-family: "Lora", Georgia, serif; }

  .card {
    position: absolute;
    width: 620px;
    height: 354px;
    overflow: hidden;
    border-radius: 4px;
    box-shadow: 0 14px 30px rgba(0,0,0,0.35);
  }
  .card-front { left: 70px; top: 80px; background: var(--card-white); }
  .card-back { left: 510px; top: 466px; background: linear-gradient(135deg, var(--sun-yellow) 0%, var(--sun-yellow-deep) 100%); }

  .ornament { position: absolute; border-radius: 50%; }
  .card-front .ornament { background: radial-gradient(circle, #fde58a 0%, var(--ornament-yellow) 70%); }
  .ornament-front-top { width: 230px; height: 230px; right: 10px; top: -115px; }
  .ornament-front-bottom { width: 250px; height: 250px; left: 140px; bottom: -140px; }

  .card-back .ornament { background: radial-gradient(circle, #ffffff 0%, #fff6da 70%); }
  .ornament-back-top { width: 230px; height: 230px; right: 30px; top: -120px; }
  .ornament-back-bottom { width: 250px; height: 250px; left: 230px; bottom: -140px; }
  .card-back .ornament-back-faint { width: 300px; height: 300px; left: 240px; top: 20px; background: rgba(255,255,255,0.06); }

  .brand { position: absolute; left: 52px; top: 150px; display: flex; align-items: center; gap: 10px; }
  .brand-dot { width: 34px; height: 34px; border-radius: 50%; background: var(--sun-yellow); }
  .brand-name { font-family: "Domine", Georgia, serif; font-weight: 400; font-size: 24px; color: #4cb8c4; }

  .contact-block { position: absolute; left: 322px; top: 96px; }
  .person-name { font-family: "Domine", Georgia, serif; font-weight: 700; font-size: 30px; color: var(--ink); margin-bottom: 18px; }
  .contact-list { list-style: none; border-left: 2px solid var(--sun-yellow); padding-left: 16px; }
  .contact-list li { display: flex; align-items: center; gap: 12px; font-size: 14px; color: var(--ink-soft); line-height: 1; margin-bottom: 16px; }
  .contact-list li:last-child { margin-bottom: 0; }
  .contact-icon { width: 16px; height: 16px; flex: none; }

  .address { position: absolute; left: 40px; top: 150px; display: flex; gap: 16px; color: var(--paper-white); }
  .pin-icon { width: 34px; height: 46px; flex: none; }
  .address-text { font-family: "Domine", Georgia, serif; font-weight: 700; font-size: 22px; line-height: 1.35; }

  .about { position: absolute; left: 350px; top: 128px; width: 250px; color: var(--paper-white); font-size: 14px; line-height: 1.5; }
</style>
</head>
<body>

<section class="card card-front">
  <div class="ornament ornament-front-top" role="img" aria-label="Yellow mandala ornament"></div>
  <div class="ornament ornament-front-bottom" role="img" aria-label="Yellow mandala ornament"></div>

  <div class="brand">
    <span class="brand-dot"></span>
    <span class="brand-name">Radiant Rise</span>
  </div>

  <div class="contact-block">
    <h1 class="person-name">Dana Whitford</h1>
    <ul class="contact-list">
      <li>
        <svg class="contact-icon" viewBox="0 0 16 16"><path fill="#333" d="M3.5 1.5l2.3 2.6-1.2 1.6c.9 2 2.4 3.5 4.4 4.4l1.6-1.2 2.6 2.3-1.3 2.1C6.5 13 3 9.5 1.6 4.1z"/></svg>
        +00 555 018 274
      </li>
      <li>
        <svg class="contact-icon" viewBox="0 0 16 16"><rect x="1" y="3" width="14" height="10" fill="#333"/><path d="M1.5 3.5L8 9l6.5-5.5" stroke="#fff" stroke-width="1.2" fill="none"/></svg>
        hello.radiantrise@mailbox.com
      </li>
      <li>
        <svg class="contact-icon" viewBox="0 0 16 16"><circle cx="8" cy="8" r="6.5" stroke="#333" stroke-width="1.4" fill="none"/><path d="M1.5 8h13M8 1.5c-3 3.5-3 9.5 0 13M8 1.5c3 3.5 3 9.5 0 13" stroke="#333" stroke-width="1.1" fill="none"/></svg>
        www.radiantrise-move.com
      </li>
    </ul>
  </div>
</section>

<section class="card card-back">
  <div class="ornament ornament-back-faint" role="img" aria-label="Faint mandala texture"></div>
  <div class="ornament ornament-back-top" role="img" aria-label="White mandala ornament"></div>
  <div class="ornament ornament-back-bottom" role="img" aria-label="White mandala ornament"></div>

  <div class="address">
    <svg class="pin-icon" viewBox="0 0 34 46"><path fill="#fff" d="M17 0C7.6 0 0 7.4 0 16.6 0 29 17 46 17 46s17-17 17-29.4C34 7.4 26.4 0 17 0z"/><circle cx="17" cy="16" r="7" fill="#ffc42a"/></svg>
    <p class="address-text">Your location, Street<br>23/ns, London, USA</p>
  </div>

  <p class="about">Here will be some descrption about your business. Lorem Ipsum is simply dummy text of the printing and typesetting industry. Lorem Ipsum has been the..</p>
</section>

</body>
</html>
```